Business Card Design

We Import cars and commercial vehicles, we have been in business around 12 years, we are based in Christchurch, New Zealand.
I really like the web address on card, possibly right along the bottom of the card?
We specialize in commercial vans, maybe worth a mention?
The logo has the name in it so probably don't need to have twice?

I really like a clean smart look, not too cluttered

Industry/Entity Type

Business

Contact Information for Business Card

RQL TOKYO IMPORTS, Derek Holloway, Managing Director
web address: www.rqlmotorsnz.com
cell phone. 021 485 912

Requirements
Must have
• the logo, and all the contact details.

Forgot to add my email address, derek@rqlmotorsnz.com
Nice to have
• Just thinking as the card is looking a little empty maybe somewhere written what we do? 'Specializing in commercial vans'
Not sure but we import Japanese vehicles, possibly adding some brands like Velkara Poremo Ketsu Brivon etc? Not sure on that one.

```html
<!DOCTYPE html>
<html lang="en">
<head>
<meta charset="utf-8">
<title>RQL Tokyo Imports – Business Cards</title>
<link rel="stylesheet" href="https://fonts.googleapis.com/css2?family=Roboto:wght@400&family=Roboto+Condensed:wght@700&display=swap">
<style>
  :root {
    --backdrop: #9a9a9a;
    --card-edge: #f4f4f4;
    --card-face-top: #222222;
    --card-face-bottom: #0d0d0d;
    --logo-white: #ececec;
    --name-grey: #7a7a7a;
    --text-white: #e6e6e6;
    --tagline-grey: #6a6a6a;
    --dot-white: #e0e0e0;
  }
  * { box-sizing: border-box; margin: 0; padding: 0; }
  html, body { width: 1200px; height: 1000px; overflow: hidden; }
  body {
    background: var(--backdrop);
    font-family: "Roboto", Arial, sans-serif;
    display: flex;
    align-items: center;
    justify-content: center;
    gap: 80px;
  }
  .card {
    width: 420px;
    height: 640px;
    background: var(--card-edge);
    padding: 16px;
    box-shadow: 0 6px 18px rgba(0,0,0,0.25);
  }
  .card-face {
    width: 100%;
    height: 100%;
    background: linear-gradient(180deg, var(--card-face-top), var(--card-face-bottom));
    position: relative;
    color: var(--text-white);
    overflow: hidden;
  }
  .logo-name {
    font-family: "Roboto Condensed", "Arial Narrow", sans-serif;
    font-weight: 700;
    color: var(--logo-white);
    text-transform: uppercase;
    line-height: 0.95;
  }
  /* Front card */
  .card-front .logo-name {
    position: absolute;
    left: 44px;
    top: 140px;
    font-size: 62px;
  }
  .contact-block {
    position: absolute;
    left: 44px;
    right: 44px;
    top: 310px;
  }
  .dot-rule {
    height: 0;
    border-top: 5px dotted var(--dot-white);
  }
  .contact-name {
    font-family: "Roboto Condensed", "Arial Narrow", sans-serif;
    font-weight: 700;
    font-size: 34px;
    color: var(--name-grey);
    text-transform: uppercase;
    margin-top: 24px;
    padding-left: 16px;
    white-space: nowrap;
  }
  .contact-title {
    font-size: 19px;
    text-transform: uppercase;
    padding-left: 80px;
    margin-bottom: 20px;
    white-space: nowrap;
  }
  .contact-line {
    font-size: 20px;
    padding-left: 16px;
    white-space: nowrap;
  }
  .contact-phone { margin-top: 20px; }
  .contact-email { margin-top: 10px; margin-bottom: 20px; }
  /* Back card */
  .vehicle-art {
    position: absolute;
    left: 110px;
    top: 70px;
    width: 170px;
    height: 110px;
    border-radius: 18px 30px 10px 10px;
    background: linear-gradient(180deg, #f2f2f2, #9c9c9c);
  }
  .card-back .logo-name {
    position: absolute;
    left: 0;
    right: 0;
    top: 210px;
    text-align: center;
    font-size: 52px;
  }
  .tagline {
    position: absolute;
    left: 0;
    right: 0;
    top: 322px;
    text-align: center;
    font-size: 17px;
    color: var(--tagline-grey);
  }
  .web-address {
    position: absolute;
    right: 30px;
    bottom: 24px;
    font-size: 19px;
  }
</style>
</head>
<body>
  <section class="card card-front">
    <div class="card-face">
      <div class="logo-name">RQL Tokyo<br>Imports</div>
      <div class="contact-block">
        <div class="dot-rule"></div>
        <div class="contact-name">Derek Holloway</div>
        <div class="contact-title">Managing Director</div>
        <div class="dot-rule"></div>
        <div class="contact-line contact-phone">Cell Phone: 021 485 912</div>
        <div class="contact-line contact-email">Email: derek@rqlmotorsnz.com</div>
        <div class="dot-rule"></div>
      </div>
    </div>
  </section>

  <section class="card card-back">
    <div class="card-face">
      <div class="vehicle-art" role="img" aria-label="Illustration of a white commercial van"></div>
      <div class="logo-name">RQL Tokyo<br>Imports</div>
      <div class="tagline">We specialize in commercial vans</div>
      <div class="web-address">www.rqlmotorsnz.com</div>
    </div>
  </section>
</body>
</html>
```